Briefpapier und Visitenkarten
Zielgruppe
In erster Linie mir selbst.
Aufgabenstellung
Gestaltung von Visitenkarten und Briefpapier.
Visitenkarten: Gestaltung beidseitig und in Pantone Farben
Briefpapier: Gestaltung einseitig und in Pantone Farben
Briefpapier und Visitenkarten sollen ein Design haben.

```html
<!DOCTYPE html>
<html lang="de">
<head>
<meta charset="utf-8">
<title>Korland Werbeagentur – Visitenkarte</title>
<link rel="stylesheet" href="https://fonts.googleapis.com/css2?family=Didact+Gothic&display=swap">
<style>
  :root {
    --stage: #1f1f21;
    --card: #bebec2;
    --card-edge: #a9a9ad;
    --ink: #77777b;
    --ink-soft: #8a8a8e;
    --mark-light: #f2f2f2;
    --lockup: #d9d9d9;
    --lockup-mark: #bcbcbc;
  }
  * { box-sizing: border-box; margin: 0; padding: 0; }
  html, body { width: 1200px; height: 1200px; overflow: hidden; }
  body {
    background: var(--stage);
    font-family: "Didact Gothic", "Century Gothic", sans-serif;
    position: relative;
  }
  .card {
    position: absolute;
    top: 200px;
    width: 560px;
    height: 370px;
    background: var(--card);
    border: 1px solid var(--card-edge);
  }
  .card--front { left: 20px; }
  .card--back { left: 620px; }

  .front-mark {
    position: absolute;
    right: 36px;
    bottom: 40px;
    display: flex;
    align-items: center;
    gap: 14px;
  }
  .front-mark__circle {
    width: 96px; height: 96px;
    border-radius: 50%;
    border: 3px solid var(--mark-light);
  }
  .front-mark__name {
    color: var(--mark-light);
    font-size: 15px;
    letter-spacing: 1px;
    text-transform: uppercase;
    line-height: 1.3;
  }

  .back-mark__circle {
    position: absolute;
    left: 40px; top: 158px;
    width: 54px; height: 54px;
    border-radius: 50%;
    background: var(--ink-soft);
  }
  .back-mark__name {
    position: absolute;
    left: 104px; top: 335px;
    width: 300px;
    transform-origin: left top;
    transform: rotate(-90deg);
  }
  .back-mark__name .wordmark {
    display: block;
    color: var(--ink);
    font-size: 25px;
    letter-spacing: 1.5px;
    white-space: nowrap;
  }
  .back-mark__name .tagline {
    display: block;
    color: var(--ink);
    font-size: 9px;
    letter-spacing: 6px;
    text-align: center;
    white-space: nowrap;
    margin-top: 1px;
  }
  .contact {
    position: absolute;
    right: 22px;
    text-align: right;
    color: var(--ink);
  }
  .contact--person { top: 80px; }
  .contact__name { font-size: 26px; line-height: 1.1; }
  .contact__role { font-size: 14px; color: var(--ink-soft); }
  .contact--details { top: 218px; font-size: 12.5px; line-height: 1.55; }
  .contact .sep { padding: 0 10px; }
  .contact__label { color: var(--ink-soft); }
  .contact__web { margin-top: 10px; }

  .lockup {
    position: absolute;
    left: 0; right: 0;
    top: 990px;
    text-align: center;
    color: var(--lockup);
  }
  .lockup__circle {
    width: 76px; height: 76px;
    border-radius: 50%;
    background: var(--lockup-mark);
    margin: 0 auto 12px;
  }
  .lockup__name { font-size: 36px; letter-spacing: 1.5px; }
  .lockup__tagline { font-size: 14px; letter-spacing: 9px; margin-top: 2px; }
</style>
</head>
<body>
  <section class="card card--front" aria-label="Visitenkarte Vorderseite">
    <div class="front-mark">
      <span class="front-mark__name">Korland<br>Werbeagentur</span>
      <div class="front-mark__circle"></div>
    </div>
  </section>

  <section class="card card--back" aria-label="Visitenkarte Rückseite">
    <div class="back-mark__circle"></div>
    <div class="back-mark__name">
      <span class="wordmark">KORLAND WERBEAGENTUR</span>
      <span class="tagline">IDEEN - DIE WIRKEN</span>
    </div>
    <div class="contact contact--person">
      <p class="contact__name">Jonas Mertel</p>
      <p class="contact__role">[Inhaber]</p>
    </div>
    <div class="contact contact--details">
      <p class="contact__label">Büro:</p>
      <p>Lindenallee 14<span class="sep">|</span>D-53840 Feldhausen</p>
      <p class="contact__web">www.korlandwa.de<span class="sep">|</span>info@korlandwa.de</p>
    </div>
  </section>

  <div class="lockup">
    <div class="lockup__circle"></div>
    <p class="lockup__name">KORLAND WERBEAGENTUR</p>
    <p class="lockup__tagline">IDEEN - DIE WIRKEN</p>
  </div>
</body>
</html>
```